Business Card for a Candle Company. - Creative Hipster Styling :)

I am after a two sided Business Card. Contact information on the front, text that will be supplied (and details further on here) on the back. Ideally I am looking for someone I can continue to work with in the future for flyers, labels, marketing material etc.

I have a Logo which I am using as the labels for the candle and have attached all the versions of the file I was given. I am after a similar feel to my logo and love the font and the feather used. it is important that my card looks like it is meant to go with the logo.

I would love you to use your imagination and see what can be thought up :)

All my candles are either clear or black glass and packaging is black and labels are white, on a square label with black writing (see attachments)

I love the feather on the logo if it can be incorporated great, if the business card looks better without it than that is fine too..

Target Market(s)

I am a new candle company and the feel I'm going for is a little luxury a little hipster. Imagine the candle going into a converted warehouse studio in the city.

Industry/Entity Type

Home And Garden

Contact Information for Business Card

I have a Logo which I am using as the labels for the candle and have attached all the versions of the file I was given. I am after a similar feel to my logo and love the font used but its caps and I don't really want everything in CAPS. It is important thought that everything goes together.

I love the feather on the logo if it can be incorporated great, if the business card looks better without it than that is fine too.

Norrel Glow Co
Harbour Reach, NSW Australia
A little wax company, in a garage, on the coast.
craftmarketa.com/au/shop/NorrelGlowCo
sociallinka.com.au/norrelglowco
norrelglowco@mailbrook.com.au
Jess Pendell
0481 276 152.

On the back of the card I need it to look good and go with the design on the front but want a bit of text;

To give you an idea of what I want on the back I've put what I've got following but I'm still working on grammar and wording so it may change slightly before the final edit.

We would love to see how you display your candle or reuse the glass vessel and would love to see a photo!
Check out ideas and share yours on your social media #norrelglowco

Just a few ideas to reuse your vessel;

A Vase to Display fresh flowers
Lolly Jar for your favourite candy
Decorate with baubles at Christmas
Bathroom Vanity Storage
Decorate with eggs at Easter
Plant a teranium inside.

Font styles to use
Decorative
Script
Other font styles liked:
• OctinVintageFree

Colors
000000
ffffff
757575

Requirements
Must have
• The only must is that it needs to look like it goes with my logo which I am using as the labels on the actual candle. the labels are white with black details and are square.
• Not too structured if possible as it is a creative company rather that a professional services company.
• I want people to pick up the card and think it looks great. I believe a business card is a very useful marketing tool and should be used as such. One card will be included in with each candle so that customers can re order.
Nice to have
• I love the feather on the logo if it can be incorporated great, if the business card looks better without it than that is fine too.
• Card just needs to fit with the logo.
Should not have
• It should not be a boring card. :)

```html
<!DOCTYPE html>
<html lang="en">
<head>
<meta charset="utf-8">
<title>Norrel Glow Co – Business Card</title>
<link href="https://fonts.googleapis.com/css2?family=Roboto+Slab:wght@300;400;700&family=Dancing+Script:wght@500&display=swap" rel="stylesheet">
<style>
  :root {
    --ink: #000000;
    --paper: #ffffff;
    --grey: #757575;
    --card-black: #0a0a0a;
    --stage: #e6e4e1;
    --feather-light: rgba(255,255,255,0.26);
    --feather-dark: rgba(255,255,255,0.03);
  }
  * { box-sizing: border-box; margin: 0; padding: 0; }
  html, body {
    width: 1200px; height: 913px; overflow: hidden;
    background: var(--stage);
  }
  .stage { position: relative; width: 1200px; height: 913px; }
  .card {
    position: absolute;
    width: 540px; height: 318px;
    border-radius: 16px;
    background: linear-gradient(150deg, #1c1c1c 0%, var(--card-black) 45%, #000 100%);
    color: var(--paper);
    font-family: "Roboto Slab", Georgia, serif;
    overflow: hidden;
    box-shadow: 0 10px 28px rgba(0,0,0,0.25);
  }
  .card--front { left: 40px; top: 120px; }
  .card--back { left: 620px; top: 475px; }

  .feather-art {
    position: absolute; z-index: 0;
    border-radius: 50% 50% 50% 50% / 60% 60% 40% 40%;
    background: linear-gradient(120deg, var(--feather-light), var(--feather-dark));
    transform: rotate(-28deg);
  }
  .card--front .feather-art { width: 290px; height: 100px; left: 250px; top: 120px; }
  .card--back .feather-art { width: 240px; height: 80px; left: 290px; top: 30px; }

  .card > *:not(.feather-art) { z-index: 1; }

  .brand {
    position: absolute;
    display: flex; align-items: center; gap: 10px;
  }
  .brand__mark {
    width: 14px; height: 14px; border-radius: 50%;
    background: var(--paper);
  }
  .brand__name {
    font-weight: 400; font-size: 24px; letter-spacing: 2px;
    color: var(--paper); white-space: nowrap;
  }
  .card--front .brand { left: 34px; top: 92px; }
  .card--back .brand { left: 50px; top: 68px; }

  .owner {
    position: absolute; right: 34px; top: 24px; text-align: right;
  }
  .owner__name { font-weight: 700; font-size: 19px; letter-spacing: 0.5px; }
  .owner__role { font-weight: 300; font-size: 12px; margin-top: 2px; }

  .divider {
    position: absolute; height: 1px; background: var(--paper);
  }
  .divider--top { left: 250px; top: 158px; width: 265px; transform: rotate(-13deg); transform-origin: left; opacity: 0.8; }
  .divider--mid { left: 34px; top: 196px; width: 220px; opacity: 0.7; }

  .location {
    position: absolute; left: 34px; top: 168px;
    font-size: 14px; letter-spacing: 0.6px; white-space: nowrap;
  }
  .contacts {
    position: absolute; left: 34px; top: 208px;
    list-style: none; font-size: 12.5px; line-height: 22px; font-weight: 300;
  }
  .contacts li { display: flex; align-items: center; gap: 9px; white-space: nowrap; }
  .contacts svg { width: 11px; height: 11px; flex: none; }

  .band {
    position: absolute; left: 0; top: 146px; width: 100%; height: 20px;
    background: var(--paper); color: var(--ink);
    font-family: "Dancing Script", cursive; font-size: 14px;
    display: flex; align-items: center; padding-left: 40px; white-space: nowrap;
  }
  .ideas {
    position: absolute; left: 0; right: 0; top: 184px;
    list-style: none; text-align: center;
    font-size: 13px; line-height: 19px; letter-spacing: 0.4px; font-weight: 300;
  }
</style>
</head>
<body>
<main class="stage">

  <section class="card card--front" aria-label="Business card front">
    <div class="feather-art" role="img" aria-label="Large finely drawn white feather illustration"></div>
    <div class="divider divider--top"></div>
    <div class="owner">
      <p class="owner__name">Jess Pendell</p>
      <p class="owner__role">Owner</p>
    </div>
    <div class="brand">
      <span class="brand__mark"></span>
      <span class="brand__name">Norrel Glow Co</span>
    </div>
    <p class="location">Harbour Reach, NSW Australia</p>
    <div class="divider divider--mid"></div>
    <ul class="contacts">
      <li>
        <svg viewBox="0 0 12 12"><path d="M2.5 1h2l1 2.6-1.3 1a6 6 0 0 0 3.2 3.2l1-1.3L11 7.5v2c0 .8-.7 1.5-1.5 1.5A8.5 8.5 0 0 1 1 2.5C1 1.7 1.7 1 2.5 1z" fill="#fff"/></svg>
        0481 276 152
      </li>
      <li>
        <svg viewBox="0 0 12 12"><rect x="0.8" y="2.3" width="10.4" height="7.4" fill="none" stroke="#fff" stroke-width="1.1"/><path d="M1 2.6 6 6.6l5-4" fill="none" stroke="#fff" stroke-width="1.1"/></svg>
        norrelglowco@mailbrook.com.au
      </li>
      <li>
        <svg viewBox="0 0 12 12"><circle cx="6" cy="6" r="5" fill="#fff"/></svg>
        sociallinka.com.au/norrelglowco
      </li>
      <li>
        <svg viewBox="0 0 12 12"><circle cx="6" cy="6" r="5" fill="none" stroke="#fff" stroke-width="1"/><ellipse cx="6" cy="6" rx="2.2" ry="5" fill="none" stroke="#fff" stroke-width="1"/><path d="M1 6h10" stroke="#fff" stroke-width="1"/></svg>
        www.craftmarketa.com/au/shop/NorrelGlowCo
      </li>
    </ul>
  </section>

  <section class="card card--back" aria-label="Business card back">
    <div class="feather-art" role="img" aria-label="Large finely drawn white feather illustration"></div>
    <div class="brand">
      <span class="brand__mark"></span>
      <span class="brand__name">Norrel Glow Co</span>
    </div>
    <p class="band">A little wax company, in a garage, on the coast</p>
    <ul class="ideas">
      <li>A Vase to Display fresh flowers</li>
      <li>Lolly Jar for your favourite candy</li>
      <li>Decorate with baubles at Christmas</li>
      <li>Bathroom Vanity Storage</li>
      <li>Decorate with eggs at Easter</li>
      <li>Plant a teranium inside.</li>
    </ul>
  </section>

</main>
</body>
</html>
```